Candidate Table Page

Need our intranet page redesigned. The layout is perfect and doesn't need to change. But the whole page doesn't seem to fit well together. Please change the font, feel, and table borders to make a more professional and easy user interface. symbols and/or icons are okay.

Target Market(s)

company staff

Industry/Entity Type

Security Guard

Coding

Coded - Design and coding required

Number of Pages Required

1 page

Font styles to use
Sans Serif

Colors
0255a3
fece3e

Requirements
Must have
• the employee information and columns
Nice to have
• icons and maybe symbols.

```html
<!DOCTYPE html>
<html lang="en">
<head>
<meta charset="utf-8">
<title>Candidates – Sentinel Guard Services</title>
<link href="https://fonts.googleapis.com/css2?family=Arimo:wght@400;700&family=Open+Sans:wght@400;600;700&display=swap" rel="stylesheet">
<style>
:root{
  --blue:#2a5f9e;
  --link:#2f5f9a;
  --row-alt:#bcd7f3;
  --ink:#222;
  --footer:#f2dc6f;
  --pager:#d6d6d6;
  --field:#e4e4e4;
}
*{box-sizing:border-box;margin:0;padding:0}
html,body{width:1200px;height:612px;overflow:hidden;background:#fff;font-family:"Open Sans",Arial,sans-serif;color:var(--ink)}
.page{position:relative;width:1200px;height:612px}

.brand{position:absolute;left:14px;top:14px;display:flex;align-items:center;gap:8px}
.brand-mark{width:26px;height:26px;border-radius:50%;background:var(--blue)}
.brand-name{color:var(--blue);font-family:"Arimo",Arial,sans-serif;font-weight:400;font-size:14px;white-space:nowrap}

.sidebar{position:absolute;left:19px;top:56px;width:172px;list-style:none;font-family:"Arimo",Arial,sans-serif}
.sidebar li{height:23.5px;margin-bottom:1.5px;background:var(--blue);color:#fff;font-size:11.5px;display:flex;align-items:center;justify-content:space-between;padding:0 6px 0 5px}
.sidebar svg{width:8px;height:8px}

.toolbar{position:absolute;left:212px;top:18px;width:973px;height:22px;font-size:11.5px;font-family:"Arimo",Arial,sans-serif}
.toolbar > *{position:absolute;top:0;height:22px;display:flex;align-items:center}
.field{background:var(--field);border:1px solid #bbb;height:18px!important;top:2px!important;font-size:8.5px;color:#666;padding:0 4px;justify-content:space-between}
.field svg{width:7px;height:5px}
.text-input{background:#fff;border:1px solid #333;height:18px!important;top:2px!important}
.btn{background:var(--blue);color:#fff;font-weight:700;font-size:8.5px;justify-content:center;height:20px!important;top:1px!important;border-radius:2px}
.user{font-size:10.5px;right:26px}
.power{width:21px;height:22px!important;right:0;background:var(--blue);justify-content:center;border-radius:2px}

.grid{position:absolute;left:211px;top:48px;width:975px;border:1px solid #ccc}
.row{display:grid;grid-template-columns:72px 164px 84px 85px 122px 90px 68px 56px 57px 39px 39px 97px;height:21.9px;align-items:center;font-size:8.2px;border-bottom:1px solid #e3e3e3}
.row > span{padding-left:7px;white-space:nowrap;overflow:hidden}
.row.head{background:var(--blue);color:#fff;font-size:7px;font-weight:600;height:20px;text-transform:uppercase;border:0}
.row.head span{display:flex;align-items:center;gap:3px}
.row.head svg{width:7px;height:7px}
.row:nth-child(odd):not(.head){background:var(--row-alt)}
.name{font-weight:600}
.tel{color:var(--link)}
.notes{display:flex;align-items:center;gap:3px}
.notes svg{width:7px;height:7px}

.pager{position:relative;height:30px;background:var(--pager);margin:1px 3px 3px;font-size:8.5px}
.pager > span{position:absolute;top:0;height:30px;display:flex;align-items:center}
.pager .nav{top:6px;width:18px;height:18px;justify-content:center;background:#fff}
.pager .nav.next{background:var(--blue)}
.pager .current{text-decoration:underline;color:var(--link)}
</style>
</head>
<body>
<div class="page">

  <div class="brand">
    <span class="brand-mark"></span>
    <span class="brand-name">Sentinel Guard Services</span>
  </div>

  <ul class="sidebar">
    <li>Home</li>
    <li>Human Resource <svg viewBox="0 0 8 8"><path d="M1 3l3 3 3-3" fill="none" stroke="#fff"/></svg></li>
    <li>Recruiting <svg viewBox="0 0 8 8"><path d="M1 3l3 3 3-3" fill="none" stroke="#fff"/></svg></li>
    <li>Inventory <svg viewBox="0 0 8 8"><path d="M1 3l3 3 3-3" fill="none" stroke="#fff"/></svg></li>
    <li>Contracts <svg viewBox="0 0 8 8"><path d="M1 3l3 3 3-3" fill="none" stroke="#fff"/></svg></li>
    <li>Supervision <svg viewBox="0 0 8 8"><path d="M1 3l3 3 3-3" fill="none" stroke="#fff"/></svg></li>
    <li>Reports <svg viewBox="0 0 8 8"><path d="M1 3l3 3 3-3" fill="none" stroke="#fff"/></svg></li>
    <li>Settings <svg viewBox="0 0 8 8"><path d="M1 3l3 3 3-3" fill="none" stroke="#fff"/></svg></li>
    <li>Organisation Chart</li>
  </ul>

  <div class="toolbar">
    <span style="left:0">Search By:</span>
    <span class="field" style="left:75px;width:78px">Name <svg viewBox="0 0 7 5"><path d="M0 0h7L3.5 5z" fill="#777"/></svg></span>
    <span class="text-input" style="left:156px;width:132px"></span>
    <span class="btn" style="left:291px;width:62px">Find</span>
    <span class="btn" style="left:356px;width:62px">Reset</span>
    <span style="left:458px">Job:</span>
    <span class="field" style="left:482px;width:94px">ALL <svg viewBox="0 0 7 5"><path d="M0 0h7L3.5 5z" fill="#777"/></svg></span>
    <span style="left:580px">Status:</span>
    <span class="field" style="left:615px;width:73px">ALL <svg viewBox="0 0 7 5"><path d="M0 0h7L3.5 5z" fill="#777"/></svg></span>
    <span style="left:692px">Office:</span>
    <span class="field" style="left:724px;width:112px">ALL <svg viewBox="0 0 7 5"><path d="M0 0h7L3.5 5z" fill="#777"/></svg></span>
    <span class="user">Omar Haddad</span>
    <span class="power"><svg width="13" height="13" viewBox="0 0 14 14"><path d="M4.2 3.5a5 5 0 1 0 5.6 0" fill="none" stroke="#fff" stroke-width="1.6"/><path d="M7 1v6" stroke="#fff" stroke-width="1.6"/></svg></span>
  </div>

  <div class="grid">
    <div class="row head">
      <span><svg viewBox="0 0 8 8"><rect x="0.5" y="1.5" width="7" height="6" fill="none" stroke="#fff"/><path d="M0.5 3h7" stroke="#fff"/></svg>Created</span>
      <span><svg viewBox="0 0 8 8"><rect x="0.5" y="0.5" width="7" height="7" fill="none" stroke="#fff"/><circle cx="4" cy="3.2" r="1.2" fill="#fff"/></svg>Name</span>
      <span><svg viewBox="0 0 8 8"><rect width="8" height="8" rx="1" fill="#fff"/></svg>Phone</span>
      <span><svg viewBox="0 0 8 8"><rect x="1.5" y="0.5" width="5" height="7" rx="1" fill="none" stroke="#fff"/></svg>Cell</span>
      <span><svg viewBox="0 0 8 8"><path d="M4 8L1.2 4a3 3 0 1 1 5.6 0z" fill="#fff"/></svg>City,State</span>
      <span><svg viewBox="0 0 8 8"><rect x="0.5" y="0.5" width="7" height="7" fill="none" stroke="#fff"/><path d="M2 4l1.5 1.5L6 2.5" fill="none" stroke="#fff"/></svg>Status</span>
      <span><svg viewBox="0 0 8 8"><rect x="0.5" y="0.5" width="7" height="7" fill="none" stroke="#fff"/></svg>Notes</span>
      <span>Reason</span>
      <span>Reactivate</span>
      <span>Retest</span>
      <span>Rehire</span>
      <span>Job Position</span>
    </div>

    <div class="row"><span>23-Jun-17</span><span class="name">Aaron Vale</span><span class="tel">(760)-555-0108</span><span class="tel">(760)-555-0178</span><span>Hesperia,California</span><span>Qualified</span><span class="notes">Notes <svg viewBox="0 0 8 8"><path d="M1 7l1-3 4-4 2 2-4 4z" fill="var(--link)"/></svg></span><span></span><span></span><span></span><span></span><span>Un-Armed Guard</span></div>
    <div class="row"><span>22-Jun-17</span><span class="name">Wesley Ward</span><span class="tel">(510)-555-0154</span><span class="tel">(510)-555-0144</span><span>San Leandro,California</span><span>Qualified</span><span class="notes">Notes <svg viewBox="0 0 8 8"><path d="M1 7l1-3 4-4 2 2-4 4z" fill="var(--link)"/></svg></span><span></span><span></span><span></span><span></span><span>Un-Armed Guard</span></div>
    <div class="row"><span>23-Jun-17</span><span class="name">Anjali Reed</span><span class="tel">(206)-555-0104</span><span class="tel">(206)-555-0104</span><span>Kent,Washington</span><span>Qualified</span><span class="notes">Notes <svg viewBox="0 0 8 8"><path d="M1 7l1-3 4-4 2 2-4 4z" fill="var(--link)"/></svg></span><span></span><span></span><span></span><span></span><span>Attendant</span></div>
    <div class="row"><span>21-Jun-17</span><span class="name">Brenda Lynn Hartley</span><span class="tel">(310)-555-0164</span><span class="tel">(323)-555-0174</span><span>Compton, California</span><span>Qualified</span><span class="notes">Notes <svg viewBox="0 0 8 8"><path d="M1 7l1-3 4-4 2 2-4 4z" fill="var(--link)"/></svg></span><span></span><span></span><span></span><span></span><span>Un-Armed Guard</span></div>
    <div class="row"><span>23-Jun-17</span><span class="name">Richard James Molina</span><span class="tel">(714)-555-0123</span><span class="tel">(714)-555-0105</span><span>Los Angeles,California</span><span>Qualified</span><span class="notes">Notes <svg viewBox="0 0 8 8"><path d="M1 7l1-3 4-4 2 2-4 4z" fill="var(--link)"/></svg></span><span></span><span></span><span></span><span></span><span>Un-Armed Guard</span></div>
    <div class="row"><span>22-Jun-17</span><span class="name">Justin Blake Carr-Dunn</span><span class="tel">(310)-555-0168</span><span class="tel">(310)-555-0168</span><span>Renton ,Washington</span><span>Qualified</span><span class="notes">Notes <svg viewBox="0 0 8 8"><path d="M1 7l1-3 4-4 2 2-4 4z" fill="var(--link)"/></svg></span><span></span><span></span><span></span><span></span><span>Un-Armed Guard</span></div>
    <div class="row"><span>23-Jun-17</span><span class="name">Debra Colton</span><span class="tel">(206)-555-0182</span><span class="tel">(206)-555-0182</span><span>Hesperia,California</span><span>Qualified</span><span class="notes">Notes <svg viewBox="0 0 8 8"><path d="M1 7l1-3 4-4 2 2-4 4z" fill="var(--link)"/></svg></span><span></span><span></span><span></span><span></span><span>Un-Armed Guard</span></div>
    <div class="row"><span>21-Jun-17</span><span class="name">Ernesto Vidal</span><span class="tel">(323)-555-0166</span><span class="tel">(323)-555-0129</span><span>San Leandro,California</span><span>Qualified</span><span class="notes">Notes <svg viewBox="0 0 8 8"><path d="M1 7l1-3 4-4 2 2-4 4z" fill="var(--link)"/></svg></span><span></span><span></span><span></span><span></span><span>Un-Armed Guard</span></div>
    <div class="row"><span>23-Jun-17</span><span class="name">Aaron Vale</span><span class="tel">(310)-555-0164</span><span class="tel">(323)-555-0174</span><span>Kent,Washington</span><span>Qualified</span><span class="notes">Notes <svg viewBox="0 0 8 8"><path d="M1 7l1-3 4-4 2 2-4 4z" fill="var(--link)"/></svg></span><span></span><span></span><span></span><span></span><span>Attendant</span></div>
    <div class="row"><span>22-Jun-17</span><span class="name">Wesley Ward</span><span class="tel">(714)-555-0123</span><span class="tel">(714)-555-0105</span><span>Compton, California</span><span>Qualified</span><span class="notes">Notes <svg viewBox="0 0 8 8"><path d="M1 7l1-3 4-4 2 2-4 4z" fill="var(--link)"/></svg></span><span></span><span></span><span></span><span></span><span>Un-Armed Guard</span></div>
    <div class="row"><span>23-Jun-17</span><span class="name">Anjali Reed</span><span class="tel">(310)-555-0168</span><span class="tel">(310)-555-0168</span><span>Los Angeles,California</span><span>Qualified</span><span class="notes">Notes <svg viewBox="0 0 8 8"><path d="M1 7l1-3 4-4 2 2-4 4z" fill="var(--link)"/></svg></span><span></span><span></span><span></span><span></span><span>Un-Armed Guard</span></div>
    <div class="row"><span>21-Jun-17</span><span class="name">Brenda Lynn Hartley</span><span class="tel">(206)-555-0182</span><span class="tel">(206)-555-0182</span><span>Renton ,Washington</span><span>Qualified</span><span class="notes">Notes <svg viewBox="0 0 8 8"><path d="M1 7l1-3 4-4 2 2-4 4z" fill="var(--link)"/></svg></span><span></span><span></span><span></span><span></span><span>Un-Armed Guard</span></div>
    <div class="row"><span>21-Jun-17</span><span class="name">Aaron Vale</span><span class="tel">(323)-555-0166</span><span class="tel">(323)-555-0129</span><span>Hesperia,California</span><span>Qualified</span><span class="notes">Notes <svg viewBox="0 0 8 8"><path d="M1 7l1-3 4-4 2 2-4 4z" fill="var(--link)"/></svg></span><span></span><span></span><span></span><span></span><span>Un-Armed Guard</span></div>

    <div class="pager">
      <span class="nav" style="left:4px"><svg width="8" height="8" viewBox="0 0 8 8"><path d="M6 0v8L1 4z" fill="#222"/></svg></span>
      <span class="current" style="left:32px">1</span>
      <span style="left:43.5px">2</span>
      <span style="left:55px">3</span>
      <span style="left:66.5px">4</span>
      <span style="left:78px">5</span>
      <span style="left:89.5px">6</span>
      <span style="left:101px">7</span>
      <span style="left:112.5px">8</span>
      <span style="left:124px">9</span>
      <span style="left:135.5px">10</span>
      <span style="left:152px">...</span>
      <span class="nav next" style="left:173px"><svg width="8" height="8" viewBox="0 0 8 8"><path d="M2 0v8l5-4z" fill="#fff"/></svg></span>
    </div>
  </div>

  <div style="position:absolute;left:3px;right:6px;bottom:0;height:28px;background:var(--footer);font-family:'Arimo',Arial,sans-serif;font-size:9.5px;display:flex;align-items:center;justify-content:center;color:#333" class="footer">Copyright © 2017 SENTINEL GUARD SERVICES All Rights Reserved.</div>
</div>
</body>
</html>
```